Web design

We need the design for the logo and website for a women fashion website. No coding required. The colors used should be neutral (maybe with a light touch of color), the style should be modern, slightly luxurious, not too crowded. The target market is young professionals who love trendy clothes.

Target Market(s)

Young professionals

Industry/Entity Type

Apparel

Number of Pages Required

5+ page

Font styles to use
Sans Serif
Other font styles liked:
• Montserrat, Engravers Gothic, Benton Sans, gotham-book

Colors

Designer to choose colors to be used in the design.

```html
<!DOCTYPE html>
<html lang="en">
<head>
<meta charset="utf-8">
<title>Velora – New Account</title>
<link href="https://fonts.googleapis.com/css2?family=Montserrat:wght@400;500;600;700&display=swap" rel="stylesheet">
<style>
:root{
  --ink:#111111;
  --text:#2b2b2b;
  --muted:#4a4a4a;
  --accent:#f0262b;
  --brand:#262338;
  --badge:#d8a317;
  --page:#f9f8f5;
  --footer:#f3f2f0;
  --header:#ffffff;
  --rule:#1f1f1f;
  --divider:#d6d6d6;
}
*{margin:0;padding:0;box-sizing:border-box}
html,body{width:1200px;height:1029px;overflow:hidden}
body{font-family:"Montserrat",sans-serif;color:var(--text);background:var(--page);position:relative}
.site-header{position:absolute;left:0;top:0;width:1200px;height:76px;background:var(--header);border-bottom:1px solid #e6e6e6}
.nav-link{position:absolute;top:32px;font-size:14px;font-weight:500;color:var(--ink);line-height:18px;white-space:nowrap}
.nav-link.sale{color:var(--accent)}
.brand{position:absolute;color:var(--brand);font-weight:600;white-space:nowrap;line-height:1}
.header-brand{left:0;width:1200px;text-align:center;top:24px;font-size:29px;letter-spacing:1px}
.footer-brand{left:95px;top:774px;font-size:46px;letter-spacing:1px}
.icon{position:absolute}
.lang{position:absolute;left:963px;top:34px;font-size:11px;font-weight:500;color:var(--ink)}
.badge{position:absolute;left:1087px;top:40px;width:12px;height:12px;border-radius:50%;background:var(--badge);color:#fff;font-size:8px;line-height:12px;text-align:center}
.account{position:absolute;left:0;top:76px;width:1200px;height:610px;background:var(--page)}
.title{position:absolute;left:0;width:1200px;top:58px;text-align:center;font-size:28px;font-weight:600;color:var(--ink);letter-spacing:.5px}
.intro{position:absolute;left:0;width:1200px;top:109px;text-align:center;font-size:13.5px;line-height:21px;color:var(--muted)}
.field{position:absolute;left:422px;width:355px;border-bottom:1px solid var(--rule);font-size:13.5px;color:var(--text);padding-left:1px}
.signup{position:absolute;left:422px;top:437px;width:355px;height:50px;background:#000;color:#fff;font-family:inherit;font-size:15px;font-weight:700;letter-spacing:1px;display:flex;align-items:center;justify-content:center;border:none}
.return{position:absolute;left:0;width:1200px;top:510px;text-align:center;font-size:13.5px;color:var(--text)}
.return span{border-bottom:1px solid var(--text);padding-bottom:1px}
.site-footer{position:absolute;left:0;top:686px;width:1200px;height:343px;background:var(--footer)}
.col-title{position:absolute;font-size:15px;font-weight:600;color:var(--ink);letter-spacing:.5px}
.col-link{position:absolute;font-size:13.5px;color:var(--text);white-space:nowrap}
.social{position:absolute;top:863px;width:33px;height:33px;border-radius:50%;border:1px solid #333;display:flex;align-items:center;justify-content:center}
.social::after{content:"";width:6px;height:6px;border-radius:50%;background:#222}
.divider{position:absolute;left:106px;top:954px;width:977px;height:1px;background:var(--divider)}
.legal{position:absolute;left:0;width:1200px;top:978px;text-align:center;font-size:13.5px;color:var(--text)}
</style>
</head>
<body>
<header class="site-header">
  <a class="nav-link" style="left:99px">Latest Arrivals</a>
  <a class="nav-link" style="left:217px">Clothes
    <svg width="9" height="6" viewBox="0 0 9 6" style="margin-left:2px;vertical-align:2px"><path d="M1 1l3.5 3.5L8 1" fill="none" stroke="#111" stroke-width="1.2"/></svg></a>
  <a class="nav-link" style="left:308px">VELORA Club</a>
  <a class="nav-link sale" style="left:426px">On Sale</a>
  <div class="brand header-brand">VELORA</div>
  <svg class="icon" style="left:919px;top:32px" width="17" height="17" viewBox="0 0 17 17"><circle cx="7" cy="7" r="6" fill="none" stroke="#111" stroke-width="1.4"/><path d="M11.5 11.5L16 16" stroke="#111" stroke-width="1.4"/></svg>
  <div class="lang">ENG <svg width="7" height="5" viewBox="0 0 7 5"><path d="M1 1l2.5 2.5L6 1" fill="none" stroke="#111" stroke-width="1.1"/></svg></div>
  <svg class="icon" style="left:1009px;top:30px" width="23" height="21" viewBox="0 0 23 21"><path d="M11.5 20L2.5 11A5.3 5.3 0 0 1 11.5 3.5 5.3 5.3 0 0 1 20.5 11Z" fill="none" stroke="#111" stroke-width="1.5"/></svg>
  <svg class="icon" style="left:1042px;top:29px" width="22" height="23" viewBox="0 0 22 23"><circle cx="11" cy="7" r="5.5" fill="none" stroke="#111" stroke-width="1.4"/><path d="M1 22c0-6 4.5-8.5 10-8.5s10 2.5 10 8.5" fill="none" stroke="#111" stroke-width="1.4"/></svg>
  <svg class="icon" style="left:1074px;top:28px" width="20" height="24" viewBox="0 0 20 24"><path d="M2 8h16l-1 15H3Z" fill="none" stroke="#111" stroke-width="1.4"/><path d="M6 8V5a4 4 0 0 1 8 0v3" fill="none" stroke="#111" stroke-width="1.4"/></svg>
  <div class="badge">0</div>
</header>

<main class="account">
  <h1 class="title">NEW ACCOUNT</h1>
  <p class="intro">Save payment and delivery details, view and track orders,<br>return items and your wish list favorites.</p>
  <div class="field" style="top:174px;height:37px">First Name</div>
  <div class="field" style="top:247px;height:27px">Last Name</div>
  <div class="field" style="top:302px;height:37px">Email address</div>
  <div class="field" style="top:374px;height:27px">Password</div>
  <button class="signup">SIGN UP</button>
  <a class="return"><span>Return to Store</span></a>
</main>

<footer class="site-footer"></footer>
<div class="brand footer-brand">VELORA</div>

<h3 class="col-title" style="left:439px;top:763px">HELP</h3>
<a class="col-link" style="left:439px;top:803px">Terms &amp; Conditions</a>
<a class="col-link" style="left:439px;top:829px">Privacy Policy</a>
<a class="col-link" style="left:439px;top:856px">Returns/exchanges</a>
<a class="col-link" style="left:439px;top:882px">Delivery Information</a>
<a class="col-link" style="left:439px;top:909px">FAQ</a>

<h3 class="col-title" style="left:731px;top:763px">SHOP</h3>
<a class="col-link" style="left:731px;top:803px">Tops</a>
<a class="col-link" style="left:731px;top:829px">Bootoms</a>
<a class="col-link" style="left:731px;top:856px">Intimates</a>
<a class="col-link" style="left:731px;top:882px">Dresses</a>
<a class="col-link" style="left:731px;top:909px">Swim</a>

<h3 class="col-title" style="left:956px;top:763px">CONTACT US</h3>
<svg class="icon" style="left:958px;top:794px" width="15" height="11" viewBox="0 0 15 11"><rect x=".5" y=".5" width="14" height="10" fill="#222"/><path d="M.5 .5l7 5.5 7-5.5" fill="none" stroke="#f3f2f0" stroke-width="1"/></svg>
<a class="col-link" style="left:979px;top:790px">info@velora.com</a>
<h3 class="col-title" style="left:956px;top:832px">FOLLOW US</h3>
<span class="social" style="left:953px" aria-label="Social profile"></span>
<span class="social" style="left:989px" aria-label="Social profile"></span>
<span class="social" style="left:1026px" aria-label="Social profile"></span>
<span class="social" style="left:1062px" aria-label="Social profile"></span>

<div class="divider"></div>
<p class="legal">Terms &amp; Conditions, Privacy Policy and @2021 followed by velora.</p>
</body>
</html>
```